Creative, Innovative PowerPoint Sales Deck Refresh needed

We are a technology firm in the Dallas, TX area and we need the powerpoint presentation used for our sales calls refreshed. This presentation is used in one of the first meetings we have with potential clients, so we want to make a memorable and positive impact - we want something that sets us apart from everyone else. We need 8 master slide templates created for our sales deck and a series of slides within the example sales deck need to be completely refreshed (slides 31-37 and 43 in the sample ppt file) We want a sales deck that is modern, innovative, creative, memorable and whimsical - NOT a typical boring "business" design. Colors should match or compliment the colors used in our logo. The logo in the footer of the attached sample ppt is old - it should be replaced with the newer logo attached. Please take a look at our website to get an idea of our culture and aesthetic www.quorbinlab.com
Updates

Project Deadline Extended
Reason: We have received several designs we like and we want our entire team to have time to give them full consideration before making a decision.

Target Market(s)

Business executives

Industry/Entity Type

Information Technology

Font styles to use
Sans Serif

Requirements
Must have
• Our logo and LedgerWave logo in footer
• Master Slide Templates
• Rework / redesign of slides 31-37 and 43
Nice to have
• We use Raleway font in a lot of our materials

```html
<!DOCTYPE html>
<html lang="en">
<head>
<meta charset="utf-8">
<title>LedgerWave Sales Deck – Slide Overview</title>
<link rel="stylesheet" href="https://fonts.googleapis.com/css2?family=Raleway:wght@400;500;600;700&display=swap">
<style>
:root{
  --navy:#1f3a68;
  --blue:#2d5d9f;
  --title:#2a5aa0;
  --ink:#4a4f57;
  --muted:#7a7f86;
  --board:#d9d9d9;
  --paper:#ffffff;
  --slate:#4f6d96;
  --teal:#3f9fa6;
  --orange:#e27a4c;
  --green:#4c9a82;
  --charcoal:#3c4650;
  --red:#c62828;
}
*{box-sizing:border-box;margin:0;padding:0}
html,body{width:1200px;height:1200px;overflow:hidden;background:#fff;font-family:'Raleway',sans-serif;color:var(--ink)}
.board{position:absolute;left:38px;top:60px;width:1124px;height:1080px;background:var(--board)}
.slide{position:absolute;width:358px;height:201px;background:var(--paper);overflow:hidden}
.c1{left:50px}.c2{left:422px}.c3{left:793px}
.r1{top:72px}.r2{top:286px}.r3{top:499px}.r4{top:713px}.r5{top:926px}
.head{position:absolute;left:0;top:8px;height:22px;border-left:3px solid var(--navy);padding-left:14px;font-size:16px;color:var(--title);line-height:22px;white-space:nowrap}
.brand{position:absolute;right:8px;top:8px;display:flex;align-items:center;gap:6px;font-size:6px;font-weight:700;color:var(--navy);letter-spacing:.8px}
.brand .sq{width:6px;height:6px;background:var(--navy)}
.brand .dot{width:6px;height:6px;border-radius:50%;background:var(--slate)}
.brand .q{font-weight:500;letter-spacing:0;font-size:5px}
.foot{position:absolute;left:0;right:0;bottom:0;height:2px;background:var(--navy)}
.url{position:absolute;left:6px;bottom:4px;font-size:5px;color:var(--ink)}
.pg{position:absolute;right:5px;bottom:5px;width:12px;height:11px;background:var(--navy);color:#fff;font-size:4px;text-align:center;line-height:11px}
.photo{position:absolute}
.tiny{font-size:4px;line-height:5px;color:var(--muted)}
.ico{width:12px;height:12px;background:var(--navy);display:inline-block;flex:none}
.ico.lg{width:20px;height:20px}
.bul{list-style:none}
.bul li{position:relative;padding-left:16px;font-size:7px;color:var(--ink);margin-bottom:11px;line-height:8px}
.bul li::before{content:"";position:absolute;left:0;top:2px;width:4px;height:4px;background:#b9bec6}
.bul li.plain::before{display:none}
.sub{font-size:10px;color:var(--blue);font-weight:500}
.logo-word{display:flex;gap:5px;align-items:center;font-size:11px;font-weight:600;color:var(--navy);letter-spacing:.6px;white-space:nowrap}
.logo-word i{width:12px;height:12px;background:var(--navy);display:inline-block}
</style>
</head>
<body>
<div class="board"></div>

<!-- 1 Title -->
<section class="slide c1 r1">
  <div class="photo" role="img" aria-label="Office building and city skyline in blue tones" style="left:0;top:0;width:358px;height:162px;background:linear-gradient(120deg,#2a3f63,#44618c 55%,#7f98b8)"></div>
  <div style="position:absolute;left:21px;top:78px;color:#fff;font-size:16px;font-weight:500;line-height:31px">LedgerWave Demo for Halvern Foods<br>Efficiency, Flexibility &amp; Visibility</div>
  <div style="position:absolute;left:0;top:162px;width:358px;height:39px;display:flex;align-items:center;justify-content:space-around;font-size:12px;font-weight:600;color:var(--navy)">
    <span style="display:flex;align-items:center;gap:5px"><i style="width:12px;height:12px;background:var(--navy);display:inline-block"></i>LEDGERWAVE</span>
    <span style="display:flex;align-items:center;gap:5px;font-size:8px;font-weight:500"><i style="width:14px;height:14px;border-radius:50%;background:var(--slate);display:inline-block"></i>quorbinlab</span>
    <span style="font-size:9px;color:var(--red);font-weight:700">Halvern</span>
  </div>
</section>

<!-- 2 About -->
<section class="slide c2 r1" style="background:linear-gradient(120deg,#3a5478,#5b7ca6 60%,#6f8db5)">
  <div style="position:absolute;left:206px;top:108px;color:#fff;font-size:16px;line-height:19px">About The<br>Quorbin Lab</div>
  <div style="position:absolute;left:206px;top:157px;width:52px;height:1px;background:#fff"></div>
</section>

<!-- 3 Roles -->
<section class="slide c3 r1">
  <div class="head">Roles &amp; Responsibilities</div>
  <div class="brand"><i class="sq"></i>LEDGERWAVE<i class="dot"></i><span class="q">quorbinlab</span></div>
  <div style="position:absolute;left:52px;top:46px;display:grid;grid-template-columns:repeat(3,98px);row-gap:10px;column-gap:1px">
    <div><div style="display:flex;gap:4px;align-items:center;font-size:6px;color:var(--blue)"><i class="ico"></i>Project Sponsor</div><p class="tiny" style="margin-top:6px">Overall project champion and leader. Sets strategy, monitors results and provides resources.</p></div>
    <div><div style="display:flex;gap:4px;align-items:center;font-size:6px;color:var(--blue)"><i class="ico"></i>Quality Assurance</div><p class="tiny" style="margin-top:6px">Ensures quality work products, gives direction to the team and manages the QA process.</p></div>
    <div><div style="display:flex;gap:4px;align-items:center;font-size:6px;color:var(--blue)"><i class="ico"></i>Change Management</div><p class="tiny" style="margin-top:6px">Enables transition, assesses impact of system changes and delivers training strategy.</p></div>
    <div><div style="display:flex;gap:4px;align-items:center;font-size:6px;color:var(--blue)"><i class="ico"></i>Steering Committee</div><p class="tiny" style="margin-top:6px">Sets overall project direction, supports the vision and resolves strategic issues.</p></div>
    <div><div style="display:flex;gap:4px;align-items:center;font-size:6px;color:var(--blue)"><i class="ico"></i>Project Management</div><p class="tiny" style="margin-top:6px">Weekly status meetings, reports to the committee, keeps scope on time and budget.</p></div>
    <div><div style="display:flex;gap:4px;align-items:center;font-size:6px;color:var(--blue)"><i class="ico"></i>Team Leaders/ SuperUsers</div><p class="tiny" style="margin-top:6px">Execute the project plan, identify risks, configure and test systems weekly.</p></div>
  </div>
  <div class="url">www.quorbinlab.com</div><div class="pg">Page</div><div class="foot"></div>
</section>

<!-- 4 Team -->
<section class="slide c1 r2">
  <div class="head">Meet our Team</div>
  <div class="brand"><i class="sq"></i>LEDGERWAVE<i class="dot"></i><span class="q">quorbinlab</span></div>
  <div style="position:absolute;left:50px;top:42px;display:grid;grid-template-columns:repeat(4,73px)">
    <div><div role="img" aria-label="Team member portrait" style="width:37px;height:37px;background:#9aa0a6"></div><p style="font-size:7px;color:var(--blue);margin-top:4px">Marcus Pell</p><p class="tiny" style="margin-top:8px">Managing<br>Director</p><p class="tiny" style="margin-top:5px;padding-right:4px">University degree in business, principal in ERP consulting, founder of a practice serving 150 clients over 18 years.</p></div>
    <div><div role="img" aria-label="Team member portrait" style="width:37px;height:37px;background:#a39a88"></div><p style="font-size:7px;color:var(--blue);margin-top:4px">Daniel Rook</p><p class="tiny" style="margin-top:8px">Director of<br>Support</p><p class="tiny" style="margin-top:5px;padding-right:4px">University graduate, principal consultant with extensive project management experience over 10 years.</p></div>
    <div><div role="img" aria-label="Team member portrait" style="width:37px;height:37px;background:#7d8a6e"></div><p style="font-size:7px;color:var(--blue);margin-top:4px">Owen Hale</p><p class="tiny" style="margin-top:8px">Director of<br>Delivery</p><p class="tiny" style="margin-top:5px;padding-right:4px">Degree in technical management, logistics operations and business transformation practice director.</p></div>
    <div><div role="img" aria-label="Team member portrait" style="width:37px;height:37px;background:#a8977e"></div><p style="font-size:7px;color:var(--blue);margin-top:4px">Tom Ashby</p><p class="tiny" style="margin-top:8px">VP of Sales</p><p class="tiny" style="margin-top:5px;padding-right:4px">Bachelor of science, business administration, partner and sales director with 15 years of ERP experience.</p></div>
  </div>
  <div class="url">www.quorbinlab.com</div><div class="pg">Page</div><div class="foot"></div>
</section>

<!-- 5 Integrity -->
<section class="slide c2 r2">
  <div class="head" style="height:30px;line-height:15px;font-size:13px;white-space:normal;width:240px;top:6px">Quorbin Lab – Integrity, Respect, Diligence</div>
  <div class="brand"><i class="sq"></i>LEDGERWAVE<i class="dot"></i><span class="q">quorbinlab</span></div>
  <div class="photo" role="img" aria-label="Modern conference room with long table" style="left:0;top:38px;width:358px;height:134px;background:linear-gradient(90deg,#5c6470,#3d4b63 55%,#2f4a78)"></div>
  <ul class="bul" style="position:absolute;left:209px;top:54px">
    <li style="color:#fff;font-size:6.5px;margin-bottom:9px">Headquarters in Cedar Ridge, TX</li>
    <li style="color:#fff;font-size:6.5px;margin-bottom:9px">Extensive Manufacturing Expertise</li>
    <li style="color:#fff;font-size:6.5px;margin-bottom:9px">“Tier One” ERP backgrounds</li>
    <li style="color:#fff;font-size:6.5px;margin-bottom:9px">Flexible Implementation Options</li>
    <li style="color:#fff;font-size:6.5px;margin-bottom:9px">Employee owned</li>
    <li style="color:#fff;font-size:6.5px;margin-bottom:9px">85 Customers</li>
    <li style="color:#fff;font-size:6.5px;margin-bottom:9px">25 Employees</li>
  </ul>
  <div class="url">www.quorbinlab.com</div><div class="pg">Page</div><div class="foot"></div>
</section>

<!-- 6 Velora -->
<section class="slide c3 r2">
  <div class="head">Velora Therapeutics</div>
  <div class="brand"><i class="sq"></i>LEDGERWAVE<i class="dot"></i><span class="q">quorbinlab</span></div>
  <div style="position:absolute;left:50px;top:52px;font-size:20px;color:var(--orange);font-weight:500">Velora</div>
  <div class="photo" role="img" aria-label="Black medical device product" style="left:44px;top:100px;width:80px;height:56px;background:linear-gradient(#3a3a3a,#111)"></div>
  <div style="position:absolute;left:152px;top:66px;display:grid;grid-template-columns:95px 95px;row-gap:24px;font-size:6.5px;line-height:8px;color:var(--muted)">
    <div style="display:flex;gap:5px"><i class="ico"></i>Baltimore area Biomedical company</div>
    <div style="display:flex;gap:5px"><i class="ico"></i>Platelet and plasma therapy system</div>
    <div style="display:flex;gap:5px"><i class="ico"></i>Phased 6 month implementation</div>
    <div style="display:flex;gap:5px"><i class="ico"></i><span>LedgerWave Footprint:<span style="display:block;font-size:5px;line-height:7px;margin:8px 0 0 12px">Financials<br>Order Entry<br>Manufacturing<br>Procurement<br>CRM</span></span></div>
  </div>
  <div class="url">www.quorbinlab.com</div><div class="pg">Page</div><div class="foot"></div>
</section>

<!-- 7 Product Demonstration -->
<section class="slide c1 r3">
  <div class="photo" role="img" aria-label="Team working at a whiteboard with sticky notes" style="left:0;top:0;width:206px;height:201px;background:linear-gradient(135deg,#c9ccd0,#8e949b 60%,#5f6670)"></div>
  <div class="logo-word" style="position:absolute;right:8px;top:8px;font-size:10px"><i></i>LEDGERWAVE</div>
  <div style="position:absolute;left:224px;top:94px;font-size:13px;font-weight:600;color:var(--blue);line-height:16px">Product<br>Demonstration</div>
  <div style="position:absolute;left:276px;top:178px;display:flex;gap:5px;align-items:center;font-size:6px"><i style="width:12px;height:12px;border-radius:50%;background:var(--slate);display:inline-block"></i>quorbinlab</div>
</section>

<!-- 8 Phase One overview -->
<section class="slide c2 r3">
  <div class="head" style="top:8px">Phase One Methodology</div>
  <div class="brand"><i class="sq"></i>LEDGERWAVE<i class="dot"></i><span class="q">quorbinlab</span></div>
  <svg style="position:absolute;left:74px;top:48px" width="210" height="44" viewBox="0 0 210 44">
    <g fill="none" stroke-width="3.5">
      <circle cx="22" cy="22" r="19" stroke="#c7d2e0"/><circle cx="63" cy="22" r="19" stroke="var(--navy)"/><circle cx="104" cy="22" r="19" stroke="var(--slate)"/><circle cx="145" cy="22" r="19" stroke="#c7d2e0"/><circle cx="186" cy="22" r="19" stroke="var(--slate)"/>
    </g>
    <g fill="var(--navy)"><circle cx="22" cy="22" r="12"/><circle cx="63" cy="22" r="12"/><circle cx="104" cy="22" r="12"/><circle cx="145" cy="22" r="12"/><circle cx="186" cy="22" r="12"/></g>
    <g fill="#fff"><rect x="18" y="17" width="8" height="10"/><rect x="58" y="18" width="10" height="8"/><rect x="99" y="18" width="10" height="8"/><rect x="140" y="18" width="10" height="8"/><circle cx="186" cy="22" r="4.5"/></g>
  </svg>
  <div style="position:absolute;left:75px;top:100px;display:grid;grid-template-columns:repeat(5,41px);font-size:5.5px;text-align:center;line-height:7px;color:var(--muted)">
    <span>Project<br>Initiation</span><span>Solution<br>Design</span><span>Application<br>Configuration</span><span>Testing &amp;<br>Preparation</span><span>Deployment &amp;<br>Support</span>
  </div>
  <div style="position:absolute;left:64px;top:136px;display:flex;gap:24px">
    <div style="width:61px;height:36px;background:#fff;box-shadow:0 1px 3px rgba(0,0,0,.25);border-top:4px solid #c7d2e0;font-size:5px;color:var(--blue);text-align:center;padding-top:12px;line-height:6px">Change<br>Management</div>
    <div style="width:61px;height:36px;background:#fff;box-shadow:0 1px 3px rgba(0,0,0,.25);border-top:4px solid #c7d2e0;font-size:5px;color:var(--blue);text-align:center;padding-top:12px;line-height:6px">User<br>Involvement</div>
    <div style="width:61px;height:36px;background:#fff;box-shadow:0 1px 3px rgba(0,0,0,.25);border-top:4px solid #c7d2e0;font-size:5px;color:var(--blue);text-align:center;padding-top:12px;line-height:6px">Program<br>Management</div>
  </div>
  <div class="url">www.quorbinlab.com</div><div class="pg">Page</div><div class="foot"></div>
</section>

<!-- 9 Five key areas -->
<section class="slide c3 r3">
  <div class="head" style="font-size:13.5px">Five Key Areas of User Adoption</div>
  <div class="brand"><i class="sq"></i>LEDGERWAVE<i class="dot"></i><span class="q">quorbinlab</span></div>
  <svg style="position:absolute;left:126px;top:56px" width="100" height="100" viewBox="0 0 100 100">
    <g fill="none" stroke-width="24" transform="rotate(-90 50 50)">
      <circle cx="50" cy="50" r="38" stroke="var(--teal)" stroke-dasharray="47.7 191" stroke-dashoffset="0"/>
      <circle cx="50" cy="50" r="38" stroke="var(--charcoal)" stroke-dasharray="47.7 191" stroke-dashoffset="-47.7"/>
      <circle cx="50" cy="50" r="38" stroke="var(--orange)" stroke-dasharray="47.7 191" stroke-dashoffset="-95.5"/>
      <circle cx="50" cy="50" r="38" stroke="var(--green)" stroke-dasharray="47.7 191" stroke-dashoffset="-143.2"/>
      <circle cx="50" cy="50" r="38" stroke="#cfd2d5" stroke-dasharray="47.7 191" stroke-dashoffset="-191"/>
    </g>
    <circle cx="50" cy="50" r="25" fill="#fff"/>
    <text x="50" y="48" font-size="8" text-anchor="middle" fill="var(--navy)" font-family="Raleway,sans-serif" font-weight="600">Five</text>
    <text x="50" y="57" font-size="8" text-anchor="middle" fill="var(--navy)" font-family="Raleway,sans-serif" font-weight="600">Key</text>
  </svg>
  <div style="font-size:9px;color:var(--navy)">
    <span style="position:absolute;left:202px;top:45px">Alignment</span>
    <span style="position:absolute;left:65px;top:70px">Measurement</span>
    <span style="position:absolute;left:247px;top:109px">Communication</span>
    <span style="position:absolute;left:80px;top:127px">Support</span>
    <span style="position:absolute;left:189px;top:170px">Training</span>
  </div>
  <div class="url">www.quorbinlab.com</div><div class="pg">Page</div><div class="foot"></div>
</section>

<!-- 10 Project Initiation -->
<section class="slide c1 r4">
  <div class="head" style="top:10px">Phase One Methodology</div>
  <div class="brand"><i class="sq"></i>LEDGERWAVE<i class="dot"></i><span class="q">quorbinlab</span></div>
  <div class="photo" role="img" aria-label="Hands typing on a laptop keyboard, navy tinted" style="left:0;top:57px;width:122px;height:104px;background:linear-gradient(135deg,#3d4a6a,#1f2a44)"></div>
  <div style="position:absolute;left:140px;top:58px;display:flex;gap:12px;align-items:center"><i class="ico lg"></i><span class="sub">Project Initiation</span></div>
  <ul class="bul" style="position:absolute;left:182px;top:90px;width:150px">
    <li>Conduct Kickoff Meeting</li><li>Finalize and Publish Project Schedule</li><li>Requirements Definition and Design</li><li>Requirements Traceability Matrix (RTM) Signoff</li>
  </ul>
  <div class="url">www.quorbinlab.com</div><div class="pg">Page</div><div class="foot"></div>
</section>

<!-- 11 Solution Design -->
<section class="slide c2 r4">
  <div class="head" style="top:6px">Phase One Methodology</div>
  <div class="brand"><i class="sq"></i>LEDGERWAVE<i class="dot"></i><span class="q">quorbinlab</span></div>
  <div class="photo" role="img" aria-label="Person using a tablet, soft grey tones" style="left:0;top:57px;width:122px;height:104px;background:linear-gradient(135deg,#d8dbdf,#8f959c)"></div>
  <div style="position:absolute;left:142px;top:58px;display:flex;gap:12px;align-items:center"><i class="ico lg"></i><span class="sub">Solution Design</span></div>
  <ul class="bul" style="position:absolute;left:186px;top:95px;width:165px">
    <li style="margin-bottom:7px">Map and Gap Against RTM</li>
    <li style="margin-bottom:4px">Identify Solutions for Gaps<div style="font-size:5px;line-height:6px;margin-top:7px;padding-left:10px">Custom Development<br>Phase Two Initiative<br>Business Process Change</div></li>
    <li>Business Flow Recommendation</li>
  </ul>
  <div class="url">www.quorbinlab.com</div><div class="pg">Page</div><div class="foot"></div>
</section>

<!-- 12 Deployment -->
<section class="slide c3 r4">
  <div class="head" style="top:7px">Phase One Methodology</div>
  <div class="brand"><i class="sq"></i>LEDGERWAVE<i class="dot"></i><span class="q">quorbinlab</span></div>
  <div style="position:absolute;left:27px;top:56px;display:flex;gap:14px;align-items:center"><i class="ico lg"></i><span class="sub">Deployment &amp; Support</span></div>
  <ul class="bul" style="position:absolute;left:62px;top:93px;width:135px">
    <li style="margin-bottom:9px">Setup Production Environment</li><li style="margin-bottom:12px">Convert Live Data</li><li style="margin-bottom:12px">GO-LIVE!</li><li style="margin-bottom:12px">Post Go-Live Support</li><li>Project Closeout</li>
  </ul>
  <div class="photo" role="img" aria-label="Hands on a laptop with floating screen graphics" style="left:209px;top:55px;width:149px;height:110px;background:linear-gradient(135deg,#c5d6d6,#e9eeee 60%,#b7c1c5)"></div>
  <div class="url">www.quorbinlab.com</div><div class="pg">Page</div><div class="foot"></div>
</section>

<!-- 13 Application Configuration -->
<section class="slide c1 r5">
  <div class="head" style="top:5px">Phase One Methodology</div>
  <div class="brand"><i class="sq"></i>LEDGERWAVE<i class="dot"></i><span class="q">quorbinlab</span></div>
  <div class="photo" role="img" aria-label="Laptop and phone showing a website" style="left:0;top:41px;width:358px;height:80px;background:linear-gradient(90deg,#2f3d52,#6e7f93 50%,#c8ced6)"></div>
  <div style="position:absolute;left:20px;top:134px;display:flex;gap:10px;align-items:center"><i class="ico lg"></i><span class="sub">Application Configuration</span></div>
  <ul class="bul" style="position:absolute;left:68px;top:163px;display:flex;gap:12px">
    <li style="font-size:6.5px;width:50px">System Setup</li><li style="font-size:6.5px;width:52px">Extended Prototyping</li><li style="font-size:6.5px;width:52px">Develop Test Scripts</li><li class="plain" style="font-size:6.5px;width:72px;padding-left:0">Initiate Data Cleansing and Conversion Routines</li>
  </ul>
  <div class="url">www.quorbinlab.com</div><div class="pg">Page</div><div class="foot"></div>
</section>

<!-- 14 Testing -->
<section class="slide c2 r5">
  <div class="head" style="top:6px">Phase One Methodology</div>
  <div class="brand"><i class="sq"></i>LEDGERWAVE<i class="dot"></i><span class="q">quorbinlab</span></div>
  <div style="position:absolute;left:21px;top:58px;display:flex;gap:16px;align-items:center"><i class="ico lg"></i><span class="sub">Testing &amp; Preparation</span></div>
  <ul class="bul" style="position:absolute;left:58px;top:95px;width:130px">
    <li style="font-size:6.5px;margin-bottom:6px">Unit Testing – Individual modules/functions</li>
    <li style="font-size:6.5px;margin-bottom:6px">Integration Testing – End-to-End Flow (Order to Cash)</li>
    <li style="font-size:6.5px;margin-bottom:6px">User Acceptance Testing – Mock Go-Live</li>
    <li style="font-size:6.5px;margin-bottom:12px">Full Life Cycle Simulations</li>
    <li style="font-size:6.5px">End User Training</li>
  </ul>
  <div class="photo" role="img" aria-label="Empty training room with chairs" style="left:215px;top:57px;width:143px;height:117px;background:linear-gradient(135deg,#6b6e73,#c9cbce 55%,#8a8d91)"></div>
  <div class="url">www.quorbinlab.com</div><div class="pg">Page</div><div class="foot"></div>
</section>

<!-- 15 Customer Success -->
<section class="slide c3 r5">
  <div class="photo" role="img" aria-label="Silhouettes helping each other up a mountain under a stormy sky" style="left:0;top:38px;width:358px;height:125px;background:linear-gradient(120deg,#4a5a6c,#8a99a8 50%,#2f3a46)"></div>
  <div style="position:absolute;left:27px;top:85px;color:#fff;font-size:12.5px;font-weight:600;line-height:16px">Customer Success<br>Stories</div>
  <div class="logo-word" style="position:absolute;left:10px;top:175px"><i></i>LEDGERWAVE</div>
  <div style="position:absolute;right:8px;top:176px;display:flex;gap:5px;align-items:center;font-size:6.5px;font-weight:500;color:var(--navy)"><i style="width:14px;height:14px;border-radius:50%;background:var(--slate);display:inline-block"></i>quorbinlab</div>
</section>
</body>
</html>
```